Pricing and Packages Page

#1 Just looking for a design no coding
We Are looking for a Design of the PRICING AND PACKAGES page. The home page is just for reference material.
Winner will be contacted and possibly hired to do additional jobs.
Brightvale Real Estate needs a web page design for our bundles. We need it to be visually appeal and an emphasis placed on the premium bundle. Attached are some pngs of our current page, and a paint mock up of an idea of our layout. Please try and stay within the theme of the top menu bars of the paint file. Whites, Blues, Oranges, and Light Grays would be preferred.
Provided is a mock-up of our home screen. We want easy to read yet an initiative for people to select home listing packages on our website. Possible reference websites would be havenlot.example and plotsellhub.example or any website that has packages and pricing to choose from.
The top of the page should include the title Packages & Pricing.
Below that we want to have it easily read and illustrated that the will "Pay Nothing Until Home Sold"
Next to that a space to enter a anticipated sales price, asking the question, how much will you save. Much sure this is emphasized.
Include the bundles, which are separated into three packages, Basic, Premium and Multi-List Package. Please include the Bundle Prices of $179, $249 and $499 along with + Transaction Coordination Fee $299. Have a spot for a Get Started Button.
The boxes on the side are just an example of what to include with the prices.
Transaction Coordination Fee and All Listings Include, We just want the text display in a way where the page isnt text heavy but illustrated.
Additional Services Offered, Just a basic list with prices next to it.
Paint

```html
<!DOCTYPE html>
<html lang="en">
<head>
<meta charset="utf-8">
<title>Brightvale Real Estate – Packages &amp; Pricing</title>
<link href="https://fonts.googleapis.com/css2?family=Open+Sans:wght@400;600;700&family=Roboto+Condensed:wght@400;700&display=swap" rel="stylesheet">
<style>
:root{
  --blue:#0d56a6;
  --blue-dark:#0a4180;
  --orange:#ef5b12;
  --orange-nav:#f5821f;
  --gray-panel:#efefef;
  --gray-cell:#dcdcdc;
  --gray-label:#e7e7e7;
  --gray-btn:#6d6e70;
  --line:#c9c9c9;
  --text:#333;
  --muted:#555;
  --white:#fff;
}
*{box-sizing:border-box;margin:0;padding:0}
html,body{width:1200px;height:2264px;overflow:hidden;background:var(--white)}
body{position:relative;font-family:"Open Sans",sans-serif;color:var(--text)}
.abs{position:absolute}

/* top nav */
.topbar{left:0;top:0;width:1200px;height:45px;background:var(--blue);font-family:"Roboto Condensed",sans-serif;color:var(--white);font-size:17px}
.topbar .nav{left:57px;top:0;height:45px;display:flex;align-items:center;gap:46px;text-transform:uppercase}
.topbar .phone{left:783px;top:0;height:45px;display:flex;align-items:center;font-weight:700;font-size:19px}
.topbar .help{left:921px;top:0;width:225px;height:45px;background:var(--orange-nav);display:flex;align-items:center;justify-content:center;font-size:15px;text-transform:uppercase}

/* header */
.brand{left:57px;top:66px;display:flex;align-items:center;gap:10px;font-size:30px;font-weight:700;color:var(--blue)}
.brand .mark{width:44px;height:44px;background:var(--blue)}
.user{left:936px;top:72px;width:210px;height:40px;border-radius:6px;background:#e9ecef;border:1px solid #cfd4da;display:flex;align-items:center;font-family:"Roboto Condensed",sans-serif;font-weight:700;font-size:17px;color:#333}
.user .avatar{width:52px;height:52px;border-radius:50%;background:linear-gradient(#6b5040,#c09a80);margin-left:6px;margin-top:-6px;margin-bottom:-6px;border:3px solid #fff}
.user .name{margin-left:14px}
.user svg{margin-left:auto;margin-right:14px}
.divider{left:0;top:136px;width:1200px;height:1px;background:#dcdcdc}

/* hero */
.exposure{left:57px;top:152px;font-size:22px;font-weight:600;color:#333}
.pay{left:57px;top:208px;display:flex;align-items:baseline;gap:6px;font-size:22px;color:#333}
.pay b{font-size:42px;color:var(--blue);font-weight:700}
.savings{left:57px;top:272px;width:450px;height:223px;background:var(--gray-panel)}
.savings h2{position:absolute;left:32px;top:16px;font-size:21px;font-weight:400;color:#666}
.savings .field{position:absolute;left:32px;width:385px;height:44px;background:var(--white);font-size:14px;color:#555;display:flex;align-items:center;padding-left:16px}
.savings .hint{position:absolute;left:32px;top:188px;font-size:15px;color:#666}
.map{left:566px;top:151px;width:358px;height:219px;background:linear-gradient(135deg,#2f8fd6,#1f5fb0 60%,#64b8ea)}
.map-label{left:935px;top:228px;font-size:21px;line-height:22px;color:#333}
.plan{top:415px;width:285px;height:80px;background:var(--blue);color:var(--white);text-align:center;border-radius:2px}
.plan .p{font-size:27px;margin-top:12px;line-height:32px}
.plan .fee{font-size:12px;font-weight:600}

/* compare table */
.compare{left:57px;top:531px;width:1089px}
.compare .title{height:53px;background:var(--blue);color:var(--white);display:flex;align-items:center;justify-content:center;font-size:22px;font-weight:600}
.row{display:grid;grid-template-columns:627px 153px 153px 156px;border-bottom:1px solid var(--line)}
.row>div{display:flex;align-items:center;justify-content:center;font-size:15px;color:#444;border-left:2px solid var(--white);background:var(--gray-cell)}
.row>div.label{justify-content:flex-start;padding-left:20px;border-left:0;background:var(--gray-label);line-height:22px}
.row.head>div{background:var(--orange);color:var(--white);font-size:19px;font-weight:600}
.row.head>div.label{background:var(--gray-label)}
.row.btns{border-bottom:0}
.row.btns>div.go{color:var(--white);font-size:17px;font-weight:600;background:var(--gray-btn)}
.row.btns>div.go.basic{background:var(--orange)}

/* transaction */
.h3{font-size:21px;font-weight:600;color:#333}
.tc-title{left:57px;top:1074px}
.tc-photo{left:57px;top:1117px;width:266px;height:145px;background:linear-gradient(135deg,#7a8f6a,#c9b59a 50%,#8aa4c0)}
.tc-text{left:344px;top:1112px;width:802px;font-size:13.6px;line-height:22px;color:#444}
.incl-title{left:0;top:1288px;width:1200px;text-align:center}

.feature{width:530px;height:150px}
.feature .pic{position:absolute;left:0;top:0;width:145px;height:145px;border-radius:50%;border:3px solid #cfd8e3}
.feature h4{position:absolute;left:163px;top:4px;font-size:20px;font-weight:600;color:#333}
.feature p{position:absolute;left:163px;top:42px;width:370px;font-size:13.6px;line-height:22px;color:#444}

/* bottom panels */
.services{left:57px;top:1877px;width:559px;border:1px solid #d9d9d9;border-top:0}
.services .bar{height:50px;background:var(--blue);color:var(--white);display:flex;align-items:center;padding-left:15px;font-size:22px;font-weight:600}
.services .bar span.box{width:28px;height:28px;background:var(--white);margin-left:auto;margin-right:14px}
.svc{display:grid;grid-template-columns:290px 151px 1fr;border-bottom:1px solid #d9d9d9}
.svc:last-child{border-bottom:0}
.svc>div{height:46px;display:flex;align-items:center;padding-left:17px;font-size:15px;color:#333;border-left:1px solid #d9d9d9}
.svc>div:first-child{border-left:0}
.svc>div:last-child{justify-content:center;padding-left:0}
.svc.head>div{height:35px;background:var(--orange);color:var(--white);font-size:18px;font-weight:600;justify-content:center;padding-left:0;border-left:1px solid var(--orange)}
.extras{left:649px;top:1877px;width:497px;height:275px;border:1px solid #9aa7b6}
.extras .bar{height:44px;background:var(--blue);color:var(--white);display:flex;align-items:center;padding-left:22px;font-size:22px;font-weight:400}
.extras ul{list-style:none;padding:18px 0 0 18px}
.extras li{display:flex;align-items:center;gap:12px;font-size:14px;color:#333;height:32.5px}

.footer{left:0;top:2194px;width:1200px;height:70px;background:var(--blue-dark);color:#c9d6e6;font-size:13px;display:flex;align-items:center;padding-left:60px}
</style>
</head>
<body>
<svg width="0" height="0" style="position:absolute">
  <defs>
    <symbol id="x" viewBox="0 0 20 20"><path d="M4 4L16 16M16 4L4 16" stroke="#ef5b12" stroke-width="3.6" stroke-linecap="round"/></symbol>
    <symbol id="tick" viewBox="0 0 12 12"><path d="M1.5 6.5L4.5 9.5L10.5 2.5" fill="none" stroke="#ef5b12" stroke-width="2"/></symbol>
  </defs>
</svg>

<header>
  <div class="abs topbar">
    <nav class="abs nav"><span>Search Listings</span><span>Why Choose Brightvale</span><span>Directory</span><span>Guides</span></nav>
    <div class="abs phone">+ 954-555-0188</div>
    <div class="abs help">FAQ's &nbsp;/&nbsp; Contact Us &nbsp;/&nbsp; Help</div>
  </div>
  <div class="abs brand"><span class="mark"></span>Brightvale Real Estate</div>
  <div class="abs user"><span class="avatar" role="img" aria-label="User profile photo"></span><span class="name">DANIEL R.</span>
    <svg width="12" height="8" viewBox="0 0 12 8"><path d="M0 0h12L6 8z" fill="#444"/></svg></div>
  <div class="abs divider"></div>
</header>

<section class="hero">
  <h1 class="abs exposure">Maximum Market Exposure Gurannted</h1>
  <div class="abs pay"><b>$0</b>Pay Noting Until Home Slod</div>
  <div class="abs savings">
    <h2>How much will you save?</h2>
    <div class="field" style="top:60px">$</div>
    <div class="field" style="top:125px">My Savings</div>
    <div class="hint">Enter Estimated Sales Price</div>
  </div>
  <div class="abs map" role="img" aria-label="Map of the United States with states in shades of blue"></div>
  <div class="abs map-label">Search Listing<br>by State</div>
  <div class="abs plan" style="left:571px"><div class="p">Basic &nbsp;$179</div><div class="fee">+ Transction coordintation fee $299</div></div>
  <div class="abs plan" style="left:861px"><div class="p">Premium &nbsp;$249</div><div class="fee">+ Transction coordintation fee $299</div></div>
</section>

<section class="abs compare">
  <div class="title">Most popular</div>
  <div class="row head" style="height:37px"><div class="label"></div><div>Basic</div><div>Preimum</div><div>MLS</div></div>
  <div class="row" style="height:37px"><div class="label"></div><div>$199</div><div>$249</div><div>$499</div></div>
  <div class="row" style="height:45px"><div class="label">Listing on Brightvale Real Estate.com</div><div><svg width="18" height="18"><use href="#x"/></svg></div><div><svg width="18" height="18"><use href="#x"/></svg></div><div><svg width="18" height="18"><use href="#x"/></svg></div></div>
  <div class="row" style="height:45px"><div class="label">Earn Featured listing on HomeSpot.example</div><div><svg width="18" height="18"><use href="#x"/></svg></div><div><svg width="18" height="18"><use href="#x"/></svg></div><div><svg width="18" height="18"><use href="#x"/></svg></div></div>
  <div class="row" style="height:48px"><div class="label">Photos</div><div>6</div><div>Unlimited</div><div>Unlimited</div></div>
  <div class="row" style="height:47px"><div class="label">Free Brokers Price Opinion</div><div></div><div><svg width="18" height="18"><use href="#x"/></svg></div><div><svg width="18" height="18"><use href="#x"/></svg></div></div>
  <div class="row" style="height:68px"><div class="label">Exposure on over 50+ real estate website including Nestly<br>Roofline Porchview Homes</div><div></div><div><svg width="18" height="18"><use href="#x"/></svg></div><div><svg width="18" height="18"><use href="#x"/></svg></div></div>
  <div class="row" style="height:50px"><div class="label">Ptrmium Yard Sing With Mobile ID #</div><div></div><div><svg width="18" height="18"><use href="#x"/></svg></div><div><svg width="18" height="18"><use href="#x"/></svg></div></div>
  <div class="row" style="height:47px"><div class="label">Listing on local MLS</div><div></div><div></div><div><svg width="18" height="18"><use href="#x"/></svg></div></div>
  <div class="row btns" style="height:36px"><div class="label"></div><div class="go basic">Get started</div><div class="go">Get started</div><div class="go">Get started</div></div>
</section>

<section>
  <h3 class="abs h3 tc-title">Transaction Coordinator Fees</h3>
  <div class="abs tc-photo" role="img" aria-label="Couple shaking hands with an agent in front of a sold home"></div>
  <p class="abs tc-text">Lorem ipsum dolor sit amet, consectetur adipiscing elit. Nulla scelerisque feugiat orci. Donec dictum luctus velit, ac cursus lacus laoreet vitae. Quisque feugiat aliquet commodo. Aliquam in dolor blandit, varius lorem eget, commodo libero. Nulla pellentesque magna nec leo scelerisque, nec porttitor metus consequat.<br>Lorem ipsum dolor sit amet, consectetur adipiscing elit. Nulla scelerisque feugiat orci. Donec dictum luctus velit, ac cursus lacus laoreet vitae. Quisque feugiat aliquet commodo. Aliquam in dolor blandit, varius lorem eget, commodo libero. Nulla pellentesque magna nec leo scelerisque, nec porttitor metus consequat.</p>
</section>

<section>
  <h3 class="abs h3 incl-title">All Listing Indulced</h3>
  <div class="abs feature" style="left:57px;top:1336px"><div class="pic" role="img" aria-label="Hand holding house keys" style="background:linear-gradient(135deg,#3a6fb0,#d9c2a8)"></div><h4>Only Pre Approved Byuers</h4><p>Lorem ipsum dolor sit amet, consectetur adipiscing elit. Nulla scelerisque feugiat orci. Donec dictum luctus velit, ac cursus lacus laoreet vitae. Quisque feugiat aliquet modo. Aliquam in dolor blandit, varius lorem eget,</p></div>
  <div class="abs feature" style="left:604px;top:1336px"><div class="pic" role="img" aria-label="Small model house" style="background:linear-gradient(135deg,#9aa6b2,#e6e2dc)"></div><h4>Sechedule Open House</h4><p>Lorem ipsum dolor sit amet, consectetur adipiscing elit. Nulla scelerisque feugiat orci. Donec dictum luctus velit, ac cursus lacus laoreet vitae. Quisque feugiat aliquet modo. Aliquam in dolor blandit, varius lorem eget,</p></div>
  <div class="abs feature" style="left:57px;top:1504px"><div class="pic" role="img" aria-label="Brick suburban house" style="background:linear-gradient(160deg,#8fb8e0,#a0603e 55%,#6f8f4a)"></div><h4>Customer support</h4><p>Lorem ipsum dolor sit amet, consectetur adipiscing elit. Nulla scelerisque feugiat orci. Donec dictum luctus velit, ac cursus lacus laoreet vitae. Quisque feugiat aliquet modo. Aliquam in dolor blandit, varius lorem eget,</p></div>
  <div class="abs feature" style="left:604px;top:1504px"><div class="pic" role="img" aria-label="Family by a sold sign" style="background:linear-gradient(135deg,#6d8c5a,#5a3d2e 55%,#c04030)"></div><h4>Contract Negotiation support</h4><p>Lorem ipsum dolor sit amet, consectetur adipiscing elit. Nulla scelerisque feugiat orci. Donec dictum luctus velit, ac cursus lacus laoreet vitae. Quisque feugiat aliquet modo. Aliquam in dolor blandit, varius lorem eget,</p></div>
  <div class="abs feature" style="left:57px;top:1670px"><div class="pic" role="img" aria-label="Two-storey house with a sold sign" style="background:linear-gradient(160deg,#6fa6dc,#d6dbe0 55%,#7a8f5a)"></div><h4>Listing Stat Tracking</h4><p>Lorem ipsum dolor sit amet, consectetur adipiscing elit. Nulla scelerisque feugiat orci. Donec dictum luctus velit, ac cursus lacus laoreet vitae. Quisque feugiat aliquet modo. Aliquam in dolor blandit, varius lorem eget,</p></div>
  <div class="abs feature" style="left:604px;top:1670px"><div class="pic" role="img" aria-label="Family holding a sold sign" style="background:linear-gradient(135deg,#8a6a50,#c9a888 55%,#b03a2e)"></div><h4>Step by Step Guides &amp; tools</h4><p>Lorem ipsum dolor sit amet, consectetur adipiscing elit. Nulla scelerisque feugiat orci. Donec dictum luctus velit, ac cursus lacus laoreet vitae. Quisque feugiat aliquet modo. Aliquam in dolor blandit, varius lorem eget,</p></div>
</section>

<section class="abs services">
  <div class="bar">Wiil you offer A 3% Buyers agent Commission ?<span class="box"></span></div>
  <div class="svc head"><div>Service</div><div>Price</div><div>Add</div></div>
  <div class="svc"><div>Photofeesional Photographyh</div><div>$ 1234</div><div>Add</div></div>
  <div class="svc"><div>Profesionl House stageing</div><div>$ 56874</div><div>Add</div></div>
  <div class="svc"><div>Broker Price opinion</div><div>$ 11597</div><div>Add</div></div>
  <div class="svc"><div>Premium Yard sign</div><div>$ 2576</div><div>Add</div></div>
</section>

<section class="abs extras">
  <div class="bar">Additional Service offered</div>
  <ul>
    <li><svg width="12" height="12"><use href="#tick"/></svg>Profeesional Photography of Real Estete</li>
    <li><svg width="12" height="12"><use href="#tick"/></svg>Pre-lisigin Apprasial</li>
    <li><svg width="12" height="12"><use href="#tick"/></svg>profssional House Staging</li>
    <li><svg width="12" height="12"><use href="#tick"/></svg>Pre lising propety Inspeection</li>
    <li><svg width="12" height="12"><use href="#tick"/></svg>Propertiry pricing Resport</li>
    <li><svg width="12" height="12"><use href="#tick"/></svg>Agent hosted open house 3 hours</li>
  </ul>
</section>

<footer class="abs footer">© 2014 Brightvale Real Estate &nbsp;|&nbsp; All rights reserved.</footer>
</body>
</html>
```